Digital Marketing Website Design

I need the homepage designed for my new digital marketing agency I am starting. The main goal for this homepage is to drive people to make an appointment for me to discuss their upcoming projects. Here are some examples of the layouts that I would like to emulate.
https://www.tallorchard.com/
https://www.webmerchantry.com/
https://talewick.com/
https://drmevorran.com/
https://www.neatlynestled.org/
My main focus is to attract leads that need help with running digital ads such as Chatterbook ads and Quorix Ads. I do offer other services like SEO and other things but the main focus is digital Ads.
The final design should communicate Ember Pixelry is a Digital marketing strategist building predictable revenue for small businesses through digital ads, email and marketing automation.
Target Market(s)
30-55, business owners, income 100K+, ecommerce companies, etc.
Industry/Entity Type
Digital Marketing
Number of Pages Required
2 page
Requirements
Must have
- An appealing look and feel set to drive people to make an appointment.
There needs to be a call to action button in the far right of the navigation
The same call to action in the navigation needs to be in each section on the homepage.
I need the homepage and an about us page.

```html
<!DOCTYPE html>
<html lang="en">
<head>
<meta charset="utf-8">
<title>Ember Pixelry — Homepage &amp; About Page</title>
<link rel="stylesheet" href="https://fonts.googleapis.com/css2?family=Poppins:wght@300;400;500;600;700;800&family=Open+Sans:wght@300;400;600;700&display=swap">
<style>
:root{
  --board-top:#a6f6fd;
  --board-bottom:#e6fdfe;
  --orange:#ff6a13;
  --orange-soft:#ffe2cc;
  --navy:#232a6e;
  --indigo:#2e3480;
  --ink:#111318;
  --text:#555a64;
  --muted:#8a8f99;
  --line:#e7e8ee;
  --crimson:#fe1f4e;
  --rose:#d6174a;
  --topbar:#1d1f24;
  --footer:#4a4a4c;
  --footer-dark:#2f2f31;
  --paper:#ffffff;
  --mist:#f4f5f9;
  --sand:#f4eee0;
}
*{box-sizing:border-box;margin:0;padding:0}
html,body{width:1200px;height:2482px;overflow:hidden}
body{background:linear-gradient(180deg,var(--board-top),var(--board-bottom));font-family:"Open Sans",sans-serif;color:var(--text)}
.board{position:relative;width:1245px;height:2576px;transform:scale(0.96386);transform-origin:0 0}
.page{position:absolute;background:var(--paper);overflow:hidden;box-shadow:0 0 0 1px rgba(0,0,0,.15)}
.page--home{left:62px;top:110px;width:550px;height:2408px}
.page--about{left:645px;top:110px;width:553px;height:1567px}
.abs{position:absolute}

/* top bar */
.topbar{height:27px;background:var(--topbar);display:flex;align-items:center;padding:0 8px;font-size:9.5px;color:#d8d8d8;gap:10px}
.topbar .dot{display:inline-block;width:6px;height:6px;border-radius:50%;background:var(--orange);margin-right:3px}
.topbar .social{margin-left:auto;display:flex;gap:12px}
.topbar .social i{width:8px;height:8px;border-radius:50%;background:#3b5ccc;display:block}
.page--about .topbar{height:24px}

/* nav */
.nav{height:38px;display:flex;align-items:center;padding:0 10px;border-bottom:1px solid var(--line)}
.brand{display:flex;align-items:center;gap:5px;font-family:"Poppins",sans-serif;font-weight:800;font-size:15px;color:var(--orange);letter-spacing:-.3px}
.brand .mark{width:8px;height:8px;background:var(--orange);border-radius:50%}
.menu{margin-left:auto;display:flex;gap:14px;font-size:7px;font-weight:600;color:#223;font-family:"Poppins",sans-serif;align-items:center}
.menu .active{color:var(--navy)}
.btn-appt{background:var(--navy);color:#fff;border-radius:14px;padding:6px 14px;font-size:7px;font-family:"Poppins",sans-serif;font-weight:600;box-shadow:0 2px 4px rgba(0,0,0,.3)}
.search{width:9px;height:9px;border:1.5px solid #999;border-radius:50%;margin-left:4px}

/* home hero */
.hero-home{position:relative;height:425px}
.hero-home .photo{position:absolute;left:308px;top:0;width:242px;height:250px;background:linear-gradient(160deg,#d9dde6 0%,#6a7184 35%,#1c2336 70%,#0d1220 100%)}
.eyebrow{font-family:"Poppins",sans-serif;font-size:6.5px;font-weight:600;color:#222;display:flex;align-items:center;gap:8px}
.eyebrow::before{content:"";width:22px;height:1.5px;background:var(--orange)}
.hero-title{font-family:"Poppins",sans-serif;font-weight:800;color:var(--orange);font-size:24px;line-height:32px;letter-spacing:-.6px;text-shadow:1px 2px 2px rgba(0,0,0,.25)}
.hero-lede{font-size:11px;line-height:19px;color:#222}
.btn-ghost{background:#bdbdbd;color:#fff;font-size:6.5px;text-align:center;line-height:8px;padding:5px 10px}
.btn-orange{background:var(--orange);color:#fff;font-size:7px;font-weight:600;padding:6px 13px}
.clients{position:absolute;left:20px;top:320px;width:510px;display:flex;justify-content:space-around;align-items:center}
.client{font-family:"Poppins",sans-serif;font-size:10px;font-weight:600;color:#222;text-align:center;width:110px;border-right:1px solid #ddd}
.client:last-child{border:0}
.dots{position:absolute;top:403px;left:251px;display:flex;gap:9px}
.dots i{width:4px;height:4px;border-radius:50%;background:#ccc;display:block}
.dots i:first-child{background:#888}

.banner-auto{height:170px;position:relative;background:linear-gradient(110deg,#0e1828,#1b2c44 55%,#0d1522)}
.banner-auto h2{position:absolute;left:12px;top:50px;font-family:"Open Sans",sans-serif;font-weight:300;color:#fff;font-size:26px;line-height:37px}

/* how it works */
.how{height:471px;position:relative;padding:0 6px}
.how h2{position:absolute;left:6px;top:60px;font-family:"Poppins",sans-serif;color:var(--orange);font-weight:600;font-size:19px}
.how p{font-size:8.6px;line-height:13.2px;color:#555}
.steps{position:absolute;left:6px;top:228px;display:flex;gap:12px}
.step{width:173px;height:175px;border:1px solid #eee;text-align:center;padding-top:24px}
.step svg{width:56px;height:56px}
.step h3{font-family:"Poppins",sans-serif;font-size:12px;color:#111;margin:14px 0 10px}
.step p{font-size:7.5px;line-height:14px;color:#666;padding:0 10px}

/* testimonials */
.reviews{height:395px;position:relative;background:linear-gradient(160deg,#1a2640,#243655 50%,#162238)}
.reviews h2{position:absolute;width:100%;text-align:center;top:42px;font-family:"Poppins",sans-serif;font-weight:400;font-size:14px;color:var(--orange)}
.reviews .rule{position:absolute;left:170px;top:72px;width:210px;height:1px;background:rgba(255,255,255,.3)}
.cards{position:absolute;left:17px;top:98px;display:flex;gap:11px}
.card{width:166px;height:270px;background:#fff;border-radius:3px;padding:30px 13px 0}
.stars{color:#ffb400;font-size:10px;letter-spacing:3px}
.who{display:flex;gap:8px;align-items:center;margin:2px 0 14px}
.avatar{width:26px;height:26px;border-radius:50%;background:linear-gradient(135deg,#c9ccd4,#6b6f7a)}
.who b{font-family:"Poppins",sans-serif;font-size:9px;color:#111;display:block;line-height:10px}
.who small{font-size:6.5px;color:#aaa;line-height:11px;display:block}
.card p{font-size:8.8px;line-height:14.5px;color:#777;font-weight:600}

.join{height:150px;background:#000;display:flex;align-items:center;justify-content:center;text-align:center}
.join h2{font-family:"Open Sans",sans-serif;font-weight:300;color:var(--orange);font-size:24px;line-height:27px}

/* pricing */
.pricing{height:360px;position:relative}
.pricing h2{position:absolute;width:100%;text-align:center;top:34px;font-family:"Open Sans",sans-serif;font-weight:400;font-size:25px;color:var(--orange)}
.plans{position:absolute;left:0;top:118px;display:flex;width:100%;justify-content:center;gap:0}
.plan{width:174px;height:238px;text-align:center;padding-top:58px}
.plan h3{font-family:"Poppins",sans-serif;font-weight:500;font-size:12px;color:#111}
.price{font-family:"Poppins",sans-serif;color:var(--crimson);font-size:24px;font-weight:500;margin:16px 0 10px}
.price sup{font-size:9px;vertical-align:12px}
.price small{font-size:9px;color:#888}
.plan ul{list-style:none;font-size:7px;color:#888;line-height:12px}
.plan .choose{display:inline-block;margin-top:26px;border:1px solid var(--crimson);border-radius:12px;padding:6px 20px;font-size:6.5px;font-weight:700;color:#222;background:#fff}
.plan--featured{background:var(--crimson);color:#fff}
.plan--featured h3,.plan--featured .price,.plan--featured .price small,.plan--featured ul{color:#fff}
.plan--featured .choose{color:var(--crimson);border-color:#fff}
.handshot{height:219px;background:linear-gradient(180deg,#0a1430,#1d3a78 55%,#0b1534)}

/* footer */
.footer{height:123px;background:var(--footer);position:relative;color:#ddd}
.footer .brand{position:absolute;left:6px;top:8px;font-size:13px}
.footer .addr{position:absolute;left:6px;top:48px;font-size:6px;line-height:10px}
.footer .soc{position:absolute;left:6px;top:94px;display:flex;gap:10px}
.footer .soc i{width:7px;height:7px;border-radius:50%;background:#3b62d8;display:block}
.fcol{position:absolute;top:6px}
.fcol h4{font-family:"Poppins",sans-serif;color:var(--orange);font-size:7.5px;font-weight:500;letter-spacing:.8px;margin-bottom:11px}
.fcol li{list-style:none;font-size:6.3px;line-height:15.6px;display:flex;align-items:center;gap:4px}
.fcol li::before{content:"";width:5px;height:5px;border-radius:50%;background:var(--crimson)}
.copy{height:30px;background:var(--footer-dark);text-align:center;font-size:6.5px;line-height:30px;color:#aaa}

/* about page */
.hero-about{height:268px;position:relative;background:linear-gradient(120deg,#0e1a2f,#1c3150 45%,#0b1222 80%)}
.hero-about .eyebrow{position:absolute;left:6px;top:65px;color:#fff;font-size:8px}
.hero-about h1{position:absolute;left:6px;top:114px;font-family:"Poppins",sans-serif;font-weight:700;color:#fff;font-size:19.5px;line-height:25px;letter-spacing:-.4px}
.hero-about p{position:absolute;left:6px;top:176px;width:330px;font-size:7.2px;line-height:13px;color:#eee}
.about{height:315px;position:relative;background:var(--mist)}
.about .eyebrow{position:absolute;left:14px;top:56px;font-size:7.5px;font-weight:500}
.about h2{position:absolute;left:14px;top:67px;font-family:"Poppins",sans-serif;font-size:15px;font-weight:700;color:#111}
.about p{position:absolute;left:14px;width:250px;font-size:7.3px;line-height:13px;color:#333}
.about .photo{position:absolute;left:277px;top:53px;width:276px;height:205px;background:linear-gradient(135deg,#2a3a5a,#8fa0bc 50%,#e6e9ef)}
.play{position:absolute;left:117px;top:83px;width:40px;height:40px;border-radius:50%;background:var(--orange);opacity:.9}
.services{height:316px;position:relative;background:var(--sand)}
.services h2{position:absolute;width:100%;text-align:center;top:53px;font-family:"Poppins",sans-serif;font-size:18px;font-weight:600;color:#101634}
.services .intro{position:absolute;width:100%;text-align:center;top:86px;font-size:7.5px;line-height:13px;color:#333}
.services .dash{position:absolute;left:262px;top:122px;width:30px;height:2px;background:var(--orange)}
.svc-row{position:absolute;left:11px;top:180px;display:flex;gap:11px}
.svc{width:170px;height:109px;background:#fff;position:relative;padding:14px 0 0 48px}
.svc .ico{position:absolute;left:10px;top:12px;width:30px;height:30px;border-radius:50%;background:#fff;box-shadow:0 2px 6px rgba(0,0,0,.15);display:flex;align-items:center;justify-content:center}
.svc h3{font-family:"Poppins",sans-serif;font-size:9px;line-height:11px;color:#111}
.svc p{margin-top:16px;font-size:7.2px;line-height:13px;color:var(--rose);padding-right:4px}
.offer{height:214px;position:relative;background:linear-gradient(120deg,var(--indigo),#2a2f78 60%,#343a8a)}
.offer h2{position:absolute;left:8px;top:58px;font-family:"Poppins",sans-serif;font-weight:400;color:#fff;font-size:18.5px;letter-spacing:-.3px}
.offer p{position:absolute;left:8px;top:92px;width:350px;font-size:9px;line-height:15px;color:#fff}
.offer .btn{position:absolute;left:8px;top:131px;width:106px;height:31px;border-radius:16px;background:var(--orange);color:#fff;font-size:7px;font-weight:700;text-align:center;line-height:31px}
.stats{height:238px;position:relative;display:flex;justify-content:space-around;padding:0 10px}
.stat{text-align:center;width:120px;padding-top:54px}
.stat .ring{width:54px;height:54px;border-radius:50%;background:var(--orange-soft);margin:0 auto;display:flex;align-items:center;justify-content:center}
.stat b{display:block;font-family:"Poppins",sans-serif;color:var(--orange);font-size:14px;margin-top:10px}
.stat span{display:block;font-size:7.5px;color:var(--orange);margin-top:30px}
</style>
</head>
<body>
<div class="board">

<!-- ===== Homepage ===== -->
<main class="page page--home">
  <div class="topbar">
    <span><i class="dot"></i>+1 (415)-208-3371</span>
    <span><i class="dot"></i>hello@emberpixelry.com</span>
    <span><i class="dot"></i>218 Harlow St, Brookfield 40217</span>
    <span class="social"><i></i><i></i><i></i><i></i></span>
  </div>
  <nav class="nav">
    <div class="brand"><span class="mark"></span>EMBER PIXELRY</div>
    <div class="menu"><span class="active">HOME</span><span>MENU 1</span><span>MENU 2 ▾</span><span>ABOUT US</span><span class="btn-appt">Appointment</span><span class="search"></span></div>
  </nav>

  <section class="hero-home">
    <div class="photo" role="img" aria-label="Businessman on the phone in front of a night city skyline"></div>
    <div class="abs eyebrow" style="left:8px;top:8px">EMBER PIXELRY</div>
    <h1 class="abs hero-title" style="left:8px;top:24px">We Built Profitable<br>Ad Campaigns For<br>small businesses</h1>
    <div class="abs" style="left:8px;top:137px;width:28px;height:2px;background:#3a6fd8"></div>
    <p class="abs hero-lede" style="left:8px;top:139px;width:260px">The selling system that brings in Predictable revenue through digital ads, email, and marketing automation.</p>
    <div class="abs btn-ghost" style="left:14px;top:222px;width:120px">Free Chatterbook Ads<br>Checklist</div>
    <div class="abs btn-orange" style="left:145px;top:223px">Schedule an Appointment</div>
    <div class="clients">
      <div class="client">Marlo Cove</div>
      <div class="client">The Oakhall<br>Kitchen</div>
      <div class="client">Bramble<br>Outfitters</div>
      <div class="client">Linnea Studio</div>
    </div>
    <div class="dots"><i></i><i></i><i></i><i></i></div>
  </section>

  <section class="banner-auto" role="img" aria-label="Finger touching a glowing digital globe interface">
    <h2>marketing automation<br>in your fingertip</h2>
  </section>

  <section class="how">
    <h2>How It Works</h2>
    <p class="abs" style="left:6px;top:96px;width:540px">At Ember Pixelry Solutions we know that you want to have a profitable business. In order to do that, you need a strong system that can predictably bring in sales even in bad times. The problem is there is so much out there to wade through and so many people telling you what you should do which makes you feel frustrated, lost, and flat out stressed out. We believe that businesses with great products should get the customer.</p>
    <p class="abs" style="left:6px;top:159px;width:520px">We understand the frustration which is why we are here to help you maneuver through the minutiae and create a system that flat out works.</p>
    <p class="abs" style="left:6px;top:195px">Here’s how we do it:</p>
    <div class="steps">
      <div class="step">
        <svg viewBox="0 0 56 56" fill="none" stroke="#222" stroke-width="2"><rect x="6" y="10" width="40" height="34" rx="3"/><line x1="6" y1="20" x2="46" y2="20"/><line x1="14" y1="5" x2="14" y2="14"/><line x1="24" y1="5" x2="24" y2="14"/><line x1="34" y1="5" x2="34" y2="14"/><circle cx="15" cy="28" r="3" fill="#ffb400"/><circle cx="25" cy="28" r="3" fill="#ffb400"/><circle cx="15" cy="37" r="3" fill="#ffb400"/><line x1="38" y1="26" x2="50" y2="40"/></svg>
        <h3>Step 1</h3>
        <p>Schedule an appointment to go through the basics of what you need and to find out if we are a good fit to work together.</p>
      </div>
      <div class="step">
        <svg viewBox="0 0 56 56" fill="none" stroke="#222" stroke-width="2"><circle cx="28" cy="14" r="8" fill="#ffb400"/><path d="M6 34l10-8 10 6 10-6 12 8-12 12-8-6-6 6z"/></svg>
        <h3>Step 2</h3>
        <p>Work with our team to build out your customer journey and selling system</p>
      </div>
      <div class="step">
        <svg viewBox="0 0 56 56" fill="none" stroke="#222" stroke-width="2"><circle cx="16" cy="14" r="9" fill="#ffb400"/><rect x="6" y="36" width="24" height="12"/><polyline points="10,30 22,22 32,26 48,10"/><polyline points="40,10 48,10 48,18"/><path d="M38 48v-12l8-6" stroke="#ffb400"/></svg>
        <h3>Step 3</h3>
        <p>Execute and enjoy the extra revenue!</p>
      </div>
    </div>
    <p class="abs" style="left:6px;top:430px;width:540px">So, schedule your appointment today. And in the meantime, checkout our Chatterbook ads checklist. So you can stop any poor running campaigns and fill in the gaps where they are needed.</p>
  </section>

  <section class="reviews" role="img" aria-label="Dark blue backdrop of digital marketing icons">
    <h2>What others are saying...</h2>
    <div class="rule"></div>
    <div class="cards">
      <article class="card"><div class="stars">★★★★★</div><div class="who"><div class="avatar"></div><div><b>Orin Delacourt</b><small>Founder &amp; CEO of<br>Crestline Works</small></div></div><p>Even the all-powerful Pointing has no control about the blind texts it is an almost unorthographic life One day however a small line of blind text by the name of Lorem Ipsum decided to leave for the far World of Grammar. The Big Oxmox advised her</p></article>
      <article class="card"><div class="stars">★★★★★</div><div class="who"><div class="avatar"></div><div><b>Mira Talbot</b><small>Founder &amp; CEO of<br>Crestline Works</small></div></div><p>Even the all-powerful Pointing has no control about the blind texts it is an almost unorthographic life One day however a small line of blind text by the name of Lorem Ipsum decided to leave for the far World of Grammar. The Big Oxmox advised her</p></article>
      <article class="card"><div class="stars">★★★★★</div><div class="who"><div class="avatar"></div><div><b>Hanne<br>Rowley</b><small>Founder &amp; CEO of<br>Crestline Works</small></div></div><p>Even the all-powerful Pointing has no control about the blind texts it is an almost unorthographic life One day however a small line of blind text by the name of Lorem Ipsum decided to leave for the far World of Grammar. The Big Oxmox advised her</p></article>
    </div>
  </section>

  <section class="join"><h2>Join with thousand of our satisfaction<br>customers, reach your success faster</h2></section>

  <section class="pricing">
    <h2>Pricing Plan</h2>
    <div class="plans">
      <div class="plan"><h3>Free</h3><div class="price"><sup>$</sup>00.0 <small>/Month</small></div><ul><li>Full Access Library</li><li>2 Multiple User</li><li>24/7 Support</li></ul><span class="choose">CHOOSE PLAN</span></div>
      <div class="plan plan--featured"><h3>Enterprise</h3><div class="price"><sup>$</sup>3.99 <small>/Month</small></div><ul><li>Full Access Library</li><li>6 Multiple User</li><li>24/7 Support</li></ul><span class="choose">CHOOSE PLAN</span></div>
      <div class="plan"><h3>Professional</h3><div class="price"><sup>$</sup>5.99 <small>/Month</small></div><ul><li>Full Access Library</li><li>8 Multiple User</li><li>24/7 Support</li></ul><span class="choose">CHOOSE PLAN</span></div>
    </div>
  </section>

  <section class="handshot" role="img" aria-label="Human hand reaching toward a robotic hand on blue"></section>

  <footer class="footer">
    <div class="brand"><span class="mark"></span>EMBER PIXELRY</div>
    <p class="addr">74 Quillmere Rd, Ashvale 30918<br>Tel.: +1 302 884 1150<br>Mail : studio@emberpixelry.com</p>
    <div class="soc"><i></i><i></i><i></i><i></i></div>
    <div class="fcol" style="left:213px"><h4>About Us</h4><ul><li>Terms &amp; Conditions</li><li>Privacy Policy</li><li>Service Policy</li><li>About Us</li></ul></div>
    <div class="fcol" style="left:402px"><h4>Latest News</h4><ul><li>Article 1</li><li>Article 2</li><li>Article 3</li><li>Article 4</li></ul></div>
  </footer>
  <div class="copy">© 2019, Ember Pixelry. All Rights Reserved</div>
</main>

<!-- ===== About page ===== -->
<main class="page page--about">
  <div class="topbar">
    <span><i class="dot"></i>+1 (415)-208-3371</span>
    <span><i class="dot"></i>hello@emberpixelry.com</span>
    <span><i class="dot"></i>218 Harlow St, Brookfield 40217</span>
    <span class="social"><i></i><i></i><i></i><i></i></span>
  </div>
  <nav class="nav">
    <div class="brand"><span class="mark"></span>EMBER PIXELRY</div>
    <div class="menu"><span class="active">HOME</span><span>MENU 1</span><span>MENU 2 ▾</span><span>ABOUT US</span><span class="btn-appt">Appointment</span><span class="search"></span></div>
  </nav>

  <section class="hero-about" role="img" aria-label="Robotic hand over a blurred night city">
    <div class="eyebrow">Free &amp; Impartial Advice!</div>
    <h1>Experienced In Research &amp;<br>Business Marketing!</h1>
    <p>Gone are the days when users were paying hefty fees to mobile service providers to send text messages. Users today require unlimited free texts. TextSwift is world’s firsts steps platform that enables free texting to all carriers.</p>
  </section>

  <section class="about">
    <div class="eyebrow">Know Who We Are</div>
    <h2>About Ember Pixelry</h2>
    <p style="top:100px">It’s an approach that brings together the best of financial planning and the best of investment management.</p>
    <p style="top:145px">A business strategy is the means by which it sets out to achieve desired ends. You have ideas, goals, and dreams. We have a culturally diverse, forward thinking team looking for talent like you.</p>
    <p style="top:203px">A business strategy is the means by which it sets out to achieve desired ends. You have ideas, goals, and dreams. We have a culturally diverse, forward thinking team looking for talent like you.</p>
    <div class="photo" role="img" aria-label="Team reviewing charts on a tablet"><div class="play"></div></div>
  </section>

  <section class="services">
    <h2>Our Services</h2>
    <p class="intro">A small river named Duden flows by their place and supplies it with the<br>necessary regelialia. It is a paradise</p>
    <div class="dash"></div>
    <div class="svc-row">
      <div class="svc"><span class="ico"><svg width="16" height="16" viewBox="0 0 16 16" fill="none" stroke="#333"><rect x="2" y="2" width="12" height="12"/><line x1="2" y1="6" x2="14" y2="6"/></svg></span><h3>Chatterbook Ads<br>Campaign</h3><p>A small river named Duden flow by their place and supplies with the necessary</p></div>
      <div class="svc"><span class="ico"><svg width="16" height="16" viewBox="0 0 16 16" fill="none" stroke="#333"><circle cx="8" cy="9" r="6"/><polyline points="8,5 8,9 11,10"/></svg></span><h3>Targeted Email<br>Marketing</h3><p>A small river named Duden flow by their place and supplies with the necessary</p></div>
      <div class="svc"><span class="ico"><svg width="16" height="16" viewBox="0 0 16 16" fill="none" stroke="#333"><path d="M1 7l4-3 3 2 3-2 4 3-4 4-3-2-3 2z"/></svg></span><h3>Bussiness Analyst</h3><p style="margin-top:18px">A small river named Duden flow by their place and supplies with the necessary</p></div>
    </div>
  </section>

  <section class="offer">
    <h2>We Offer Financial &amp; Superior Advices</h2>
    <p>A small river named Duden flows by their place and supplies it with the necessary regelialia. It is a paradisematic country, in which</p>
    <span class="btn">LEARN MORE</span>
  </section>

  <section class="stats">
    <div class="stat"><div class="ring"><svg width="24" height="24" viewBox="0 0 24 24" fill="none" stroke="#ff6a13" stroke-width="1.5"><circle cx="9" cy="9" r="4"/><path d="M2 21c1-5 13-5 14 0"/><rect x="14" y="3" width="8" height="5"/></svg></div><b>109,300</b><span>Support Given</span></div>
    <div class="stat"><div class="ring"><svg width="24" height="24" viewBox="0 0 24 24" fill="none" stroke="#ff6a13" stroke-width="1.5"><rect x="2" y="7" width="20" height="10"/><circle cx="12" cy="12" r="3"/></svg></div><b>10,930,118</b><span>Revenues</span></div>
    <div class="stat"><div class="ring"><svg width="24" height="24" viewBox="0 0 24 24" fill="none" stroke="#ff6a13" stroke-width="1.5"><path d="M7 3h10v6a5 5 0 0 1-10 0z"/><line x1="12" y1="14" x2="12" y2="19"/><line x1="8" y1="21" x2="16" y2="21"/></svg></div><b>16</b><span>Award</span></div>
    <div class="stat"><div class="ring"><svg width="24" height="24" viewBox="0 0 24 24" fill="none" stroke="#ff6a13" stroke-width="1.5"><rect x="3" y="10" width="4" height="10"/><path d="M7 11l5-8c2 0 2 2 1 5h7l-2 12H7"/></svg></div><b>109,300</b><span>Satisfaction Customer</span></div>
  </section>

  <footer class="footer">
    <div class="brand"><span class="mark"></span>EMBER PIXELRY</div>
    <p class="addr">74 Quillmere Rd, Ashvale 30918<br>Tel.: +1 302 884 1150<br>Mail : studio@emberpixelry.com</p>
    <div class="soc"><i></i><i></i><i></i><i></i></div>
    <div class="fcol" style="left:212px"><h4>About Us</h4><ul><li>Terms &amp; Conditions</li><li>Privacy Policy</li><li>Service Policy</li><li>About Us</li></ul></div>
    <div class="fcol" style="left:400px"><h4>Latest News</h4><ul><li>Article 1</li><li>Article 2</li><li>Article 3</li><li>Article 4</li></ul></div>
  </footer>
  <div class="copy">© 2019, Ember Pixelry. All Rights Reserved</div>
</main>

</div>
</body>
</html>
```